Wrenfield Atelier, and interior design project management company!

We invite you to participate in our logo and web design contest for "Wrenfield Atelier Management Corp."!

Here's a brief description of our company paraphrased by ChatGPT.

Company Overview:
Wrenfield Atelier Management Corp. is your trusted partner for interior design project management, guided by international standards set forth by the Ordway Planning Council (OPC) and the Structured Delivery Reference Compendium (SDREF). With a commitment to excellence, we seamlessly merge modern project management techniques with traditional values, emphasizing quality and attention to detail in every project.

Our Unique Strengths:

Local Fabrication Facility: What sets us apart is our in-house fabrication facility, a millwork shop with an impressive 20 years of experience. This facility empowers us to exercise meticulous control over the production process, ensuring that your project is crafted with precision and care right in our local community.

Experienced Skilled Workers: At Wrenfield Atelier Management Corp., our team comprises highly skilled and experienced craftsmen and artisans. They bring years of expertise to every project, guaranteeing that your interior design visions are brought to life with unmatched skill and finesse.

Serving Commercial and Residential Clients:
Our primary focus is on serving commercial clients, specializing in Tenant Improvement (TI) projects. We understand the unique demands of commercial spaces, and our project management expertise ensures that your commercial interior design projects are executed efficiently and within budget.

In addition to our commercial expertise, we also cater to discerning residential clients who seek that extra level of attention to detail. Our comprehensive services encompass all types of projects, from commercial tenant improvements to residential renovations. Regardless of the project's scale or scope, you can trust that all aspects will be managed seamlessly by our professional team.

Why Choose Us:
We are not just project managers; we are passionate advocates for your project's success. By adhering to OPC and SDREF standards, we deliver project management that is structured, efficient, and dependable. Our commitment to personal and approachable service, combined with our dedication to quality craftsmanship, ensures that your interior design projects are executed flawlessly from start to finish.

With Wrenfield Atelier Management Corp., you can trust that your project will benefit from the perfect blend of modern project management techniques and traditional values, resulting in interiors that are not only aesthetically pleasing but also built to stand the test of time.

Whether you require a commercial TI project or a residential project with meticulous attention to detail, we are the one-stop professional company that can bring your vision to life. Join our logo design contest, and let's together represent our dedication to excellence in project management and craftsmanship for both commercial and residential clients.

Target Market(s)

interior designers and architects, business owners

Industry/Entity Type

construction, project management, interior design, custom millwork and cabinets

Number of Pages Required

1 page

Requirements
Must have
• General consideration for design to float from social media to website.
Nice to have
• Consideration for more sophisticated backend support for customer support and project management update integrations apps such as ClickUp. (Technical portion not part of scope of work.)

```html
<!DOCTYPE html>
<html lang="en">
<head>
<meta charset="utf-8">
<title>Wrenfield Atelier Management Corp.</title>
<link href="https://fonts.googleapis.com/css2?family=Barlow:wght@400;500;600;700&display=swap" rel="stylesheet">
<style>
:root{
  --ink:#2b2b2b;
  --text:#555555;
  --sand:#e9d3c8;
  --cream:#f7f2ee;
  --panel:#f4efeb;
  --footer:#3a3a3a;
  --white:#ffffff;
}
*{box-sizing:border-box;margin:0;padding:0}
html,body{width:1200px;height:3712px;overflow:hidden;background:var(--white)}
body{font-family:'Barlow',sans-serif;color:var(--ink);position:relative}
.abs{position:absolute}
.header-brand{left:110px;top:26px;display:flex;align-items:center;gap:12px}
.brand-square{width:44px;height:44px;border:2px solid var(--ink)}
.brand-name{font-weight:600;font-size:21px;line-height:26px;text-transform:uppercase;color:var(--ink)}
.nav{left:609px;top:42px;display:flex;gap:32px;font-size:14px;letter-spacing:.3px}
.nav a{color:var(--ink);text-decoration:none;padding-bottom:10px}
.nav a.active{border-bottom:3px solid var(--ink)}
.photo{display:block}
.hero-photo{left:419px;top:105px;width:781px;height:535px;background:linear-gradient(135deg,#6b4a36 0%,#3a342f 40%,#8c8a86 70%,#cfc9c2 100%)}
.hero-panel{left:111px;top:347px;width:488px;height:293px;background:var(--panel)}
.hero-title{left:179px;top:420px;font-size:41px;font-weight:600;line-height:46px;text-transform:uppercase}
.btn{display:inline-block;background:var(--ink);color:var(--white);font-weight:600;font-size:14px;text-transform:uppercase;text-align:center}
.hero-btn{left:180px;top:527px;width:131px;height:41px;line-height:41px}
.slider-dots{left:49px;top:292px;display:flex;flex-direction:column;gap:30px}
.slider-dots span{width:12px;height:12px;border-radius:50%;background:var(--ink)}
.slider-dots span.current{background:var(--white);border:2px solid var(--ink);box-shadow:inset 0 0 0 2px var(--white),inset 0 0 0 6px var(--ink)}
.scroll-hint{left:0;width:1200px;top:690px;text-align:center;font-size:14px;text-transform:uppercase}
.frame{border:13px solid var(--sand)}
.about-frame{left:341px;top:765px;width:859px;height:648px;border-right:none}
.about-photo{left:111px;top:867px;width:459px;height:443px;background:linear-gradient(180deg,#6d7780 0%,#a9b3bb 45%,#3a3c3f 75%,#161616 100%)}
.section-title{font-size:40px;font-weight:600;text-transform:uppercase;line-height:1}
.about-title{left:658px;top:936px}
.body-copy{font-size:14px;line-height:25.8px;color:var(--text);text-align:justify}
.about-copy{left:658px;top:992px;width:430px}
.about-btn{left:660px;top:1196px;width:132px;height:40px;line-height:40px}
.strengths-title{left:111px;top:1537px}
.card{overflow:hidden}
.card-photo{width:100%;height:100%}
.card-caption{position:absolute;background:var(--cream);padding:14px 15px 12px}
.card-caption h3{font-size:21px;font-weight:600;text-transform:uppercase;line-height:26px;margin-bottom:10px}
.card-caption p{font-size:13.4px;line-height:21.5px;color:var(--text);text-align:justify}
.card-one{left:111px;top:1618px;width:977px;height:387px}
.card-one .card-photo{background:linear-gradient(180deg,#2c2724 0%,#8a7462 45%,#3b332d 100%)}
.card-one .card-caption{left:23px;top:243px;width:929px;height:123px}
.card-two{left:111px;top:2014px;width:480px;height:395px}
.card-two .card-photo{background:linear-gradient(180deg,#3d3935 0%,#7a7166 50%,#4e4a45 100%)}
.card-two .card-caption{left:22px;top:197px;width:437px;height:169px}
.card-three{left:601px;top:2014px;width:487px;height:395px}
.card-three .card-photo{background:linear-gradient(180deg,#121212 0%,#5a5e62 40%,#d6d8da 65%,#7c7f82 100%)}
.card-three .card-caption{left:23px;top:179px;width:439px;height:187px}
.why-frame{left:0;top:2538px;width:857px;height:649px;border-left:none}
.why-title{left:114px;top:2622px}
.why-copy{left:114px;top:2676px;width:428px}
.why-copy p+p{margin-top:26px}
.why-photo{left:630px;top:2641px;width:458px;height:442px;background:linear-gradient(135deg,#6a5a48 0%,#9a8c7a 40%,#3f3a36 75%,#2a2826 100%)}
.footer{left:0;top:3280px;width:1200px;height:432px;background:var(--footer);color:var(--white)}
.footer-brand{left:174px;top:78px;display:flex;align-items:center;gap:12px}
.footer-brand .brand-square{border-color:var(--white)}
.footer-brand .brand-name{color:var(--white)}
.footer-about{left:174px;top:154px;width:287px;font-size:12.5px;line-height:21.5px;text-align:justify}
.footer-heading{font-size:21px;font-weight:600}
.contact-heading{left:575px;top:92px}
.contact-list{left:575px;top:144px;list-style:none;font-size:13.5px;line-height:19px}
.contact-list li{display:flex;gap:12px;align-items:flex-start;margin-bottom:16px}
.contact-list svg{flex:none}
.links-heading{left:918px;top:92px}
.links-list{left:918px;top:152px;list-style:none;font-size:13.5px;line-height:21.5px}
.links-list li{display:flex;gap:16px;align-items:center}
.copyright{left:0;top:365px;width:1200px;text-align:center;font-size:13.5px}
</style>
</head>
<body>

<header>
  <div class="abs header-brand"><span class="brand-square"></span><span class="brand-name">Wrenfield Atelier<br>Management Corp</span></div>
  <nav class="abs nav"><a class="active">HOME</a><a>ABOUT</a><a>SERVICES</a><a>BLOG</a><a>PORTFOLIO</a><a>CONTACT</a></nav>
</header>

<section class="hero">
  <div class="abs photo hero-photo" role="img" aria-label="Industrial loft office with brick vaulted ceiling, black steel partitions and desks"></div>
  <div class="abs hero-panel"></div>
  <h1 class="abs hero-title">Wrenfield Atelier<br>Management Corp</h1>
  <span class="abs btn hero-btn">Get Started</span>
  <div class="abs slider-dots"><span class="current"></span><span></span><span></span><span></span></div>
  <div class="abs scroll-hint">Scroll Down<br>
    <svg width="10" height="10" viewBox="0 0 10 10"><path d="M1 1l4 3.5L9 1M1 5l4 3.5L9 5" fill="none" stroke="#2b2b2b" stroke-width="1.3"/></svg>
  </div>
</section>

<section class="about">
  <div class="abs frame about-frame"></div>
  <div class="abs photo about-photo" role="img" aria-label="Executive corner office with black desk overlooking a city skyline"></div>
  <h2 class="abs section-title about-title">About Us</h2>
  <p class="abs body-copy about-copy">Wrenfield Atelier Management Corp. is your trusted partner for interior design project management, guided by international standards set forth by the Ordway Planning Council (OPC) and the Structured Delivery Reference Compendium (SDREF). With a commitment to excellence, we seamlessly merge modern project management techniques with traditional values, emphasizing quality and attention to detail in every project.</p>
  <span class="abs btn about-btn">Learn More</span>
</section>

<section class="strengths">
  <h2 class="abs section-title strengths-title">Our Unique Strengths</h2>
  <article class="abs card card-one">
    <div class="card-photo" role="img" aria-label="Boutique retail interior with clothing rails and spotlit black ceiling"></div>
    <div class="card-caption"><h3>Local Fabrication Facility</h3><p>What sets us apart is our in-house fabrication facility, a millwork shop with an impressive 20 years of experience. This facility empowers us to exercise meticulous control over the production process, ensuring that your project is crafted with precision and care right in our local community.</p></div>
  </article>
  <article class="abs card card-two">
    <div class="card-photo" role="img" aria-label="Loft workspace with tall steel windows, pendant lamps and plants"></div>
    <div class="card-caption"><h3>Experienced Skilled Workers</h3><p>At Wrenfield Atelier Management Corp., our team comprises highly skilled and experienced craftsmen and artisans. They bring years of expertise to every project, guaranteeing that your interior design visions are brought to life with unmatched skill and finesse.</p></div>
  </article>
  <article class="abs card card-three">
    <div class="card-photo" role="img" aria-label="Modern white commercial interior with angled linear ceiling lights"></div>
    <div class="card-caption"><h3>Serving Commercial and<br>Residential Clients</h3><p>Our primary focus is on serving commercial clients, specializing in Tenant Improvement (TI) projects. We understand the unique demands of commercial spaces, and our project management expertise ensures that your commercial interior design projects are executed efficiently and within budget.</p></div>
  </article>
</section>

<section class="why">
  <div class="abs frame why-frame"></div>
  <h2 class="abs section-title why-title">Why Choose Us</h2>
  <div class="abs body-copy why-copy">
    <p>We are not just project managers; we are passionate advocates for your project's success. By adhering to OPC and SDREF standards, we deliver project management that is structured, efficient, and dependable. Our commitment to personal and approachable service, combined with our dedication to quality craftsmanship, ensures that your interior design projects are executed flawlessly from start to finish.</p>
    <p>With Wrenfield Atelier Management Corp., you can trust that your project will benefit from the perfect blend of modern project management techniques and traditional values, resulting in interiors that are not only aesthetically pleasing but also built to stand the test of time.</p>
    <p>Whether you require a commercial TI project or a residential project with meticulous attention to detail, we are the one-stop professional company that can bring your vision to life.</p>
  </div>
  <div class="abs photo why-photo" role="img" aria-label="Two smiling business partners standing in a bright office"></div>
</section>

<footer class="abs footer">
  <div class="abs footer-brand"><span class="brand-square"></span><span class="brand-name">Wrenfield Atelier<br>Management Corp</span></div>
  <p class="abs footer-about">Wrenfield Atelier Management Corp. is your trusted partner for interior design project management, guided by international standards set forth by the Ordway Planning Council (OPC) and the Structured Delivery Reference Compendium (SDREF)</p>

  <h4 class="abs footer-heading contact-heading">Contact Us</h4>
  <ul class="abs contact-list">
    <li><svg width="32" height="32" viewBox="0 0 32 32"><circle cx="16" cy="16" r="16" fill="#fff"/><path d="M16 9a5 5 0 0 0-5 5c0 4 5 9 5 9s5-5 5-9a5 5 0 0 0-5-5z" fill="#3a3a3a"/><circle cx="16" cy="14" r="1.8" fill="#fff"/></svg><span>214 Alder Row, Suite 3,<br>Brookhaven</span></li>
    <li><svg width="32" height="32" viewBox="0 0 32 32"><circle cx="16" cy="16" r="16" fill="#fff"/><path d="M12 10l3 3-2 2c1 2 2 3 4 4l2-2 3 3-2 2c-5 0-10-5-10-10z" fill="#3a3a3a"/></svg><span style="padding-top:7px">+1 555 014 2270</span></li>
    <li><svg width="32" height="32" viewBox="0 0 32 32"><circle cx="16" cy="16" r="16" fill="#fff"/><rect x="9" y="11" width="14" height="10" fill="#3a3a3a"/><path d="M9 11l7 6 7-6" fill="none" stroke="#fff" stroke-width="1.2"/></svg><span style="padding-top:7px">info@wrenfieldatelier.com</span></li>
  </ul>

  <h4 class="abs footer-heading links-heading">Quick Links</h4>
  <ul class="abs links-list">
    <li><span>»</span>Home</li><li><span>»</span>About</li><li><span>»</span>Portfolio</li><li><span>»</span>Services</li><li><span>»</span>Blog</li><li><span>»</span>Contact</li>
  </ul>

  <p class="abs copyright">Copyrights 2023 | All Rights Reserved</p>
</footer>

</body>
</html>
```